2-Sided Law Firm Business Card

This is the second phase of a law firm "rebrand project" in which I'm changing my firm's name to "Brockwyn Law PLLC." The first phase was a logo contest -- I will be updating this project sometime tomorrow with the winning logo design.

The business card will need to include, on its reverse side, the firm's logo and tag line, "Legal Practical Counsel for Growing Ventures," on a darker background whose color is consistent with the logo design.

The face of the card will need to include the firm's name (logo), website url, and phone number. It will also need to include, at the very least, the name of the attorney, the attorney's title, the attorney's email address, and the attorney's twitter feed. (I do not maintain a dedicated office and therefore the card does not need to specify a business address.) I will provide the actual contact information to the winning designer. Until then, you may use fictional data in suggesting your proposed design.

My firm specializes in representing startup companies. This means I routinely interact with young entrepreneurs and the (typically) older, more experienced investors who fund them. I need to appeal to the former without offending the latter. I'm interesting in conveying the idea that my firm is a credible alternative to larger, brand-name firms. I use these words in positioning my firm in this market: creative; flexible; fair; practical; experienced. The winning design needs to convey this idea.

I'm will also be re-working my website soon and will likely use noto sans and noto serif as my primary website fonts. I'd like the business card to use a font that is similar, but also compatible with the font used in the firm's logo.

Target Market(s)

Young entrepreneurs and older investors who collaborate in the formation and funding of high-tech startup companies located in the Pacific Northwest.

Industry/Entity Type

Law Firm

Font styles to use
Serif
Sans Serif

Requirements
Must have
• Firm logo, firm tag line, firm website url, firm phone number, attorney name, attorney title, attorney email address, and attorney twitter.

The attached pdf indicates kind of what I have in mind, recognizing that it is my amateur attempt at doing what I'm hoping the winning designer is able to do so much better.
Nice to have
• Adding a statement about my practice areas, if there's room, might be nice:

"General Counsel | Business Formation | Intellectual Property | Angel Investments & Venture Capital | Mergers & Acquisitions"

Also, I make it a point to meet with clients "by appointment only" in the following areas of Seattle: "Harbor Point | Cedar Flats | Millbrook | North Lakeview." It might be worth including as well, but only if the card itself isn't too cramped. I favor "too simple" over "too informative."
Should not have
• Do NOT put the scales of justice anywhere on this business card. I am a business lawyer.

```html
<!DOCTYPE html>
<html lang="en">
<head>
<meta charset="utf-8">
<title>Brockwyn Law PLLC — Business Card</title>
<link rel="stylesheet" href="https://fonts.googleapis.com/css2?family=Noto+Sans:wght@400;500&display=swap">
<style>
  :root {
    --navy: #1c4a7a;
    --band: #1d4f7e;
    --ink: #1a1a1a;
    --muted: #5b6067;
    --paper: #ffffff;
    --edge: #111111;
  }
  * { box-sizing: border-box; margin: 0; padding: 0; }
  html, body {
    width: 1200px; height: 786px; overflow: hidden;
    background: var(--paper);
  }
  .sheet { position: relative; width: 1200px; height: 786px; font-family: "Noto Sans", sans-serif; }

  .firm-name {
    font-family: "Noto Sans", sans-serif; font-weight: 400;
    color: var(--navy); line-height: 1; white-space: nowrap;
  }
  .firm-tagline {
    font-family: "Noto Sans", sans-serif; font-weight: 400;
    color: var(--muted); white-space: nowrap;
  }

  .showcase { position: absolute; left: 0; right: 0; top: 205px; text-align: center; }
  .showcase .firm-name { font-size: 38px; }
  .showcase .firm-tagline { font-size: 13px; margin-top: 12px; }

  .card {
    position: absolute; top: 473px; height: 313px;
    border: 1px solid var(--edge); background: var(--paper); overflow: hidden;
  }
  .card--back { left: 0; width: 599px; }
  .card--front { left: 598px; width: 602px; }
  .card__bands { position: absolute; inset: 0; width: 100%; height: 100%; }
  .card__bands polygon { fill: var(--band); }

  .back__brand { position: absolute; left: 0; right: 0; top: 140px; text-align: center; }
  .back__brand .firm-name { font-size: 25px; }
  .back__brand .firm-tagline { font-size: 9px; margin-top: 8px; }

  .front__brand {
    position: absolute; right: 318px; top: 112px; text-align: center;
  }
  .front__brand .firm-name { font-size: 14px; }
  .front__brand .firm-tagline { font-size: 6px; margin-top: 5px; }

  .front__divider {
    position: absolute; left: 296px; top: 75px; width: 1px; height: 97px;
    background: var(--navy);
  }
  .contact { position: absolute; left: 312px; top: 79px; color: var(--ink); }
  .contact__name { font-size: 14px; font-weight: 400; line-height: 1.2; }
  .contact__title { font-size: 8.5px; color: var(--navy); margin-top: 2px; }
  .contact__lines { list-style: none; margin-top: 18px; font-size: 8.5px; line-height: 1.35; }

  .front__footer {
    position: absolute; left: 0; right: 0; top: 180px; text-align: center;
    font-size: 8.5px; color: var(--ink); line-height: 1.4;
  }
  .front__areas--locations { color: var(--navy); font-weight: 500; margin-top: 7px; }
  .front__url { color: var(--navy); margin-top: 3px; }
</style>
</head>
<body>
<main class="sheet">

  <div class="showcase">
    <div class="firm-name">Brockwyn Law PLLC</div>
    <div class="firm-tagline">Practical Counsel for Growing Ventures</div>
  </div>

  <section class="card card--back" aria-label="Card reverse">
    <svg class="card__bands" viewBox="0 0 599 313" preserveAspectRatio="none" aria-hidden="true">
      <polygon points="0,17 300,3 599,17 599,29 300,10 0,29"/>
      <polygon points="0,283 300,304 599,283 599,293 300,313 0,293"/>
    </svg>
    <div class="back__brand">
      <div class="firm-name">Brockwyn Law PLLC</div>
      <div class="firm-tagline">Practical Counsel for Growing Ventures</div>
    </div>
  </section>

  <section class="card card--front" aria-label="Card face">
    <svg class="card__bands" viewBox="0 0 602 313" preserveAspectRatio="none" aria-hidden="true">
      <polygon points="0,17 301,3 602,17 602,29 301,10 0,29"/>
      <polygon points="0,283 301,304 602,283 602,293 301,313 0,293"/>
    </svg>

    <div class="front__brand">
      <div class="firm-name">Brockwyn Law PLLC</div>
      <div class="firm-tagline">Practical Counsel for Growing Ventures</div>
    </div>

    <div class="front__divider"></div>

    <div class="contact">
      <div class="contact__name">Evan R. Brockwyn</div>
      <div class="contact__title">Startup Attorney</div>
      <ul class="contact__lines">
        <li>425.555.0187</li>
        <li>evan@brockwynlawpllc.com</li>
        <li>evan brockwyn</li>
      </ul>
    </div>

    <div class="front__footer">
      <p class="front__areas">General Counsel | Business Formation | Intellectual Property</p>
      <p class="front__areas">Angel Investments &amp; Venture Capital | Mergers &amp; Acquisitions</p>
      <p class="front__areas front__areas--locations">Harbor Point | Cedar Flats | Millbrook | North Lakeview</p>
      <p class="front__url">www.brockwynpllc.com</p>
    </div>
  </section>

</main>
</body>
</html>
```